Porch Light Podcast Cover Graphic

We need a graphic designed for a new podcast called "Porch Light." The graphic will be used on multiple podcasting platforms as the lead graphic advertising the podcast. The podcast consists of interviews of individuals sharing their life experiences including challenges, successes, lessons learned, and unexpected turns. The purpose of the podcast is to help listeners and participants learn from the life experiences of everyday neighbors. This podcast has a heavy Christian foundation on the parable of the good samaritan. We believe that through hearing the experiences of everyday neighbors, listeners can be strengthened, nourished, and aided to handle their own life challenges and trials. We would like the final design to be simple and reflective of the purpose and the parable of the good samaritan. The final design needs to have the title of the podcast, "Porch Light." We believe the best designs will limit the number of colors to less than 5 and will look good in a monochromatic version as well as a color version. We think the color white should be the main color. The graphic should be square in dimensions. We have considered having two hands grasping each other as if to lift the hand from below, but open to other creative simple takes to convey the lessons from the good samaritan.

```html
<!DOCTYPE html>
<html lang="en">
<head>
<meta charset="utf-8">
<title>Porch Light Podcast Cover</title>
<link href="https://fonts.googleapis.com/css2?family=Bebas+Neue&family=Great+Vibes&family=Montserrat:wght@400;800&display=swap" rel="stylesheet">
<style>
  :root {
    --frame-yellow: #fff200;
    --title-white: #ffffff;
    --label-navy: #1b2150;
    --sky-blue: #8fb0d4;
    --sky-cream: #f3e6cf;
    --horizon-amber: #e0953a;
    --ground-dark: #140604;
  }
  html, body {
    margin: 0;
    width: 1200px;
    height: 1200px;
    overflow: hidden;
    background: var(--ground-dark);
  }
  .cover {
    position: relative;
    width: 1200px;
    height: 1200px;
    overflow: hidden;
  }
  .cover-photo {
    position: absolute;
    inset: 0;
    background:
      radial-gradient(ellipse 420px 520px at 600px 700px, rgba(150, 80, 20, 0.85), rgba(106, 53, 16, 0) 70%),
      radial-gradient(ellipse 260px 180px at 600px 330px, rgba(255, 238, 200, 0.95), rgba(255, 238, 200, 0) 70%),
      linear-gradient(180deg,
        var(--sky-blue) 0%,
        #b9c7d9 18%,
        var(--sky-cream) 30%,
        var(--horizon-amber) 40%,
        #2a0f06 46%,
        #1e0a05 70%,
        var(--ground-dark) 100%);
  }
  .frame-line {
    position: absolute;
    background: var(--frame-yellow);
  }
  .frame-top-left     { left: 40px;   top: 82px;   width: 291px; height: 7px; }
  .frame-top-right    { left: 864px;  top: 82px;   width: 296px; height: 7px; }
  .frame-left         { left: 40px;   top: 82px;   width: 7px;   height: 1029px; }
  .frame-right        { left: 1153px; top: 82px;   width: 7px;   height: 1029px; }
  .frame-bottom-left  { left: 40px;   top: 1104px; width: 254px; height: 7px; }
  .frame-bottom-right { left: 906px;  top: 1104px; width: 254px; height: 7px; }

  .cover-type {
    position: absolute;
    inset: 0;
  }
  .podcast-label {
    font-family: "Montserrat", sans-serif;
    font-weight: 400;
    font-size: 36px;
    letter-spacing: 34px;
    fill: var(--label-navy);
  }
  .title-main {
    font-family: "Bebas Neue", sans-serif;
    font-size: 390px;
    letter-spacing: 4px;
    fill: var(--title-white);
  }
  .title-script {
    font-family: "Great Vibes", cursive;
    font-size: 240px;
    fill: var(--frame-yellow);
  }
  .host-name {
    font-family: "Montserrat", sans-serif;
    font-weight: 800;
    font-size: 62px;
    fill: var(--frame-yellow);
  }
</style>
</head>
<body>
  <main class="cover">
    <div class="cover-photo" role="img" aria-label="Photo of a row of people in silhouette holding raised hands against a sunset sky"></div>

    <div class="frame-line frame-top-left"></div>
    <div class="frame-line frame-top-right"></div>
    <div class="frame-line frame-left"></div>
    <div class="frame-line frame-right"></div>
    <div class="frame-line frame-bottom-left"></div>
    <div class="frame-line frame-bottom-right"></div>

    <svg class="cover-type" width="1200" height="1200" viewBox="0 0 1200 1200">
      <text class="podcast-label" x="614" y="98" text-anchor="middle">PODCAST</text>
      <text class="title-main" x="600" y="1010" text-anchor="middle">LIGHT</text>
      <text class="title-script" x="640" y="800" text-anchor="middle" transform="rotate(-4 640 760)">Porch</text>
      <text class="host-name" x="600" y="1130" text-anchor="middle">DALEN MARSH</text>
    </svg>
  </main>
</body>
</html>
```